Graphic Design Project

Enhance the look of our home page. Please note, we do not want a complete redesign. We just want to tweak it some to optimize a user's first impression. Dev-ready files not required - a mockup will be fine (jpg or pdf).

I have attached source file for our current page.

Specific objectives:

- We really like the modern look of "www.lo.zi" website. Would like to tighten up our appearance just a little to be more similar.

- A more creative design for the 4 text boxes in the middle of the page. Currently looks sub-par and outdated. We want a modern appearance.

- Colors can be revised some if you believe it will modernize / enhance the design.

Please submit your designs as soon as possible as we are under a huge time crunch and will be making our selections early.

The winner of this contest will get a followup project as well. We have a few upcoming tasks that will require a top-notch modern designer.

Industry/Entity Type

Graphic Design

Requirements
Must have
• - We really like the modern look of "www.lo.zi" website. Would like to tighten up our appearance just a little to be more similar.

- A more creative design for the 4 text boxes in the middle of the page. Currently looks sub-par and outdated.

- Colors can be revised some if you believe it will enhance the appearance.

```html
<!DOCTYPE html>
<html lang="en">
<head>
<meta charset="utf-8">
<title>TalentReach – The Source for Networking Superstars</title>
<link href="https://fonts.googleapis.com/css2?family=Oswald:wght@300;400&family=Noto+Sans:wght@400;700&family=Roboto+Condensed:wght@400&display=swap" rel="stylesheet">
<style>
:root{
  --bg-light:#f4f4f4;
  --bg-mid:#dcdcdc;
  --steel:#4f7fa3;
  --steel-light:#7ea4c1;
  --steel-dark:#5b87a8;
  --ink:#161616;
  --panel-dark:#141414;
  --green:#4fae4a;
  --green-dark:#3e9a3a;
  --footer:#262626;
  --text-muted:#555;
  --white:#ffffff;
}
*{margin:0;padding:0;box-sizing:border-box}
html,body{width:1200px;height:878px;overflow:hidden}
body{
  position:relative;
  font-family:"Noto Sans",sans-serif;
  background:radial-gradient(ellipse at 50% 40%,var(--bg-light) 0%,#ececec 55%,var(--bg-mid) 100%);
}
.abs{position:absolute}
.brand{left:170px;top:22px}
.brand-name{font-family:"Noto Sans",sans-serif;font-weight:700;font-size:33px;color:var(--steel);letter-spacing:-.5px;line-height:1}
.brand-tagline{font-size:12.5px;color:#666;letter-spacing:.8px;margin-top:8px}
.signin-label{left:668px;top:15px;font-size:11.5px;color:#555;letter-spacing:.2px}
.account-btn{top:33px;height:34px;line-height:34px;color:var(--white);font-weight:700;font-size:12px;text-align:center;letter-spacing:.2px}
.account-btn.networkers{left:655px;width:172px;background:var(--steel-dark)}
.account-btn.business{left:845px;width:184px;background:var(--ink)}
.bg-figure{font-family:"Oswald",sans-serif;font-weight:400;color:rgba(0,0,0,.045);line-height:1}
.dots{width:56px;height:3px;background:repeating-linear-gradient(90deg,currentColor 0 5px,transparent 5px 8px)}
.hero-dots{left:254px;top:261px;color:#333}
.hero-title{left:190px;top:262px;font-family:"Oswald",sans-serif;font-size:45px;color:var(--steel);letter-spacing:-1px}
.hero-sub{left:170px;top:311px;width:288px;text-align:right;font-family:"Roboto Condensed",sans-serif;font-size:35px;color:var(--ink);letter-spacing:-2px}
.signin-btn{left:277px;top:365px;width:178px;height:52px;background:linear-gradient(var(--green),var(--green-dark));display:flex;align-items:center;justify-content:center;gap:12px;color:var(--white);font-family:"Roboto Condensed",sans-serif;font-size:32px;box-shadow:0 2px 4px rgba(0,0,0,.2)}
.signin-btn .mark{width:22px;height:22px;border-radius:50%;background:var(--white)}
.portrait{left:545px;top:85px;width:455px;height:690px;border-radius:200px 200px 0 0;background:linear-gradient(180deg,#c79a7a 0%,#b98c6e 30%,#5d6f92 55%,#3d4c72 100%);opacity:.9}
.panels{left:0;top:0}
.feature{top:510px;width:230px;color:var(--white)}
.feature .dots{color:var(--white);margin-left:26px;margin-bottom:6px}
.feature h2{font-family:"Oswald",sans-serif;font-weight:300;font-size:37px;letter-spacing:-1px;line-height:1.1}
.feature p{margin-top:12px;font-size:15px;line-height:17px;letter-spacing:.6px}
.feature.compare{left:142px}
.feature.print{left:388px}
.feature.share{left:635px}
.feature.track{left:881px}
.feature.track p{line-height:22px}
.follow-btn{top:741px;height:31px;background:linear-gradient(var(--green),var(--green-dark));color:var(--white);font-size:11px;display:flex;align-items:center;gap:10px;padding-left:8px;border-radius:3px 3px 0 0}
.follow-btn .mark{width:14px;height:14px;border-radius:50%;background:var(--white)}
.follow-btn.chirp{left:170px;width:155px}
.follow-btn.peep{left:329px;width:154px}
.footer-links{left:170px;top:791px;display:flex;font-size:10.5px;font-weight:700;color:var(--white);letter-spacing:.2px}
.footer-links span{padding:0 12px;border-left:1px solid #888;line-height:12px}
.footer-links span:first-child{padding-left:0;border:none}
.social{left:623px;top:790px;display:flex;gap:9px}
.social i{display:block;width:18px;height:18px;border-radius:50%;background:#e6e6e6}
.copyright{left:789px;top:792px;font-size:11px;color:var(--white)}
</style>
</head>
<body>
  <div class="abs bg-figure" style="left:420px;top:100px;font-size:74px">2,815</div>
  <div class="abs bg-figure" style="left:100px;top:330px;font-size:66px">38,500</div>
  <div class="abs bg-figure" style="left:212px;top:690px;font-size:52px">22%</div>

  <div class="abs portrait" role="img" aria-label="Photo of a smiling businesswoman in a pinstripe suit pointing toward the sign-in button"></div>

  <header>
    <div class="abs brand">
      <div class="brand-name">TalentReach</div>
      <div class="brand-tagline">The Source for Networking Superstars</div>
    </div>
    <div class="abs signin-label">SIGN IN OR LEARN MORE</div>
    <div class="abs account-btn networkers">NETWORKING SUPERSTARS</div>
    <div class="abs account-btn business">BUSINESS USERS/RECRUITERS</div>
  </header>

  <section class="hero">
    <div class="abs dots hero-dots"></div>
    <h1 class="abs hero-title">ACTIVATE PROFILE</h1>
    <div class="abs hero-sub">Instantly With Chirpline</div>
    <div class="abs signin-btn"><span class="mark"></span>Sign In</div>
  </section>

  <svg class="abs panels" width="1200" height="878" viewBox="0 0 1200 878">
    <defs>
      <linearGradient id="steelFill" x1="0" y1="0" x2="1" y2="1">
        <stop offset="0" stop-color="#8fb0c8"/>
        <stop offset="1" stop-color="#56809f"/>
      </linearGradient>
    </defs>
    <polygon points="128,497 373,497 332,695 86,695" fill="#141414"/>
    <polygon points="373,497 620,497 578,695 332,695" fill="url(#steelFill)"/>
    <polygon points="620,497 866,497 824,695 578,695" fill="#141414"/>
    <polygon points="866,497 1114,497 1072,695 824,695" fill="url(#steelFill)"/>
    <polygon points="86,690 1072,690 1071,695 86,695" fill="#555" opacity=".5"/>
    <polygon points="100,771 1114,771 1100,828 83,828" fill="#262626"/>
  </svg>

  <section class="features">
    <div class="abs feature compare"><div class="dots"></div><h2>COMPARE</h2><p>Against others within our database to see how you rank</p></div>
    <div class="abs feature print"><div class="dots"></div><h2>PRINT</h2><p>To strengthen and supplement your resume by showcasing actual results</p></div>
    <div class="abs feature share"><div class="dots"></div><h2>SHARE</h2><p>A link to your profile in social activity... personal branding at its best</p></div>
    <div class="abs feature track"><div class="dots"></div><h2>TRACK</h2><p>Your profile traffic with detailed statistic reporting</p></div>
  </section>

  <div class="abs follow-btn chirp"><span class="mark"></span>Follow us on Chirpline</div>
  <div class="abs follow-btn peep"><span class="mark"></span>Follow us on Peeplink</div>

  <footer>
    <nav class="abs footer-links"><span>CONTACT US</span><span>SAMPLE PROFILE</span><span>TERM OF SERVICES</span><span>PRIVACY POLICY</span></nav>
    <div class="abs social"><i></i><i></i><i></i><i></i></div>
    <div class="abs copyright">Copyright © 2013 TalentReach. All rights reserved.</div>
  </footer>
</body>
</html>
```